PLUME Residence One-Page Inserts

We need TWO one-page insert for a transplant display stand (6"x8"). We have a few furnished apartments and we need to inform our guests about the services available:

Insert #1: Delivery and Pickup Services in the neighborhood (Laundry, Groceries, Restaurants).
Insert #1 Text: "Heading: Pick and Delivery Services in your neighborhood:" Text below it: "1) Laundry Pickup - Call: +9714-382-7160. 2) Groceries Delivery - Call: +9714-382-7160, 3) Restaurants Delivery - Call: +9714-382-7160"

Insert #2: We also need another one-page insert to encourage the guests to enjoy the candles and to make the apartment have a homier feeling.
Insert #2 Text: "Heading: Feel at home. Text below it: "Dim the lights, light up a candle, play nice music, have a relaxing stay."

Target Market(s)

Staybrook Users. Apartment Guests. Tourist. Age Group 20 to 60 years old.

Industry/Entity Type

Hotel

Requirements
Must have
• - The Company logo of PLUME Residence must be displayed on the upper corner. (Logo attached). The logo should be a single color either white or black (Not red and black or red and white)
• For Insert # 1: Laundry, Groceries, and Breakfast Resturaunts images or icons. The images/icons must be unified and look like from the same family of images/icons.
• For Insert # 2: A romantic candle(s) dinner pictures.
Nice to have
• Not too many colors
• Not too busy
• Simple
• Eye Catchy
Should not have
• Lots of colors
• Too many images
• Too Busy

```html
<!DOCTYPE html>
<html lang="en">
<head>
<meta charset="utf-8">
<title>PLUME Residence Inserts</title>
<link rel="stylesheet" href="https://fonts.googleapis.com/css2?family=Open+Sans:wght@400;600;700&display=swap">
<style>
  :root {
    --page: #d6d7d9;
    --white: #ffffff;
    --ink: #2b2b2b;
    --pill: #e9e9ea;
    --night-1: #2f3034;
    --night-2: #55575c;
    --night-3: #6f6a5e;
    --ember-1: #7a3a1f;
    --ember-2: #a5542c;
    --ember-3: #d98a4a;
  }
  * { box-sizing: border-box; margin: 0; padding: 0; }
  html, body {
    width: 889px; height: 1200px; overflow: hidden;
    background: var(--page);
    font-family: "Open Sans", Arial, sans-serif;
  }
  .insert {
    position: absolute; left: 84px;
    width: 720px; height: 540px;
    overflow: hidden; color: var(--white);
    box-shadow: 0 6px 14px rgba(0,0,0,.35);
  }
  .insert--services { top: 30px; }
  .insert--home { top: 630px; }
  .insert__photo { position: absolute; inset: 0; }
  .insert--services .insert__photo {
    background:
      radial-gradient(circle at 78% 20%, rgba(160,150,110,.45), transparent 35%),
      radial-gradient(circle at 15% 15%, rgba(20,22,28,.9), transparent 40%),
      linear-gradient(160deg, var(--night-1) 0%, var(--night-2) 55%, var(--night-3) 100%);
  }
  .insert--home .insert__photo {
    background:
      radial-gradient(ellipse at 55% 85%, rgba(240,160,90,.85), transparent 55%),
      linear-gradient(180deg, var(--ember-1) 0%, var(--ember-2) 50%, var(--ember-3) 80%, var(--ember-1) 100%);
  }
  .brand {
    position: absolute; top: 62px; left: 0; width: 100%;
    text-align: center; font-size: 80px; font-weight: 400;
    letter-spacing: 2px; line-height: 1;
  }
  .headline {
    position: absolute; left: 0; width: 100%; text-align: center;
    font-weight: 600; font-size: 22px; letter-spacing: .2px;
  }
  .insert--services .headline { top: 193px; }
  .insert--home .headline { top: 180px; }
  .lede {
    position: absolute; top: 235px; left: 0; width: 100%;
    text-align: center; font-size: 16px;
  }
  .service {
    position: absolute; top: 247px; width: 220px; text-align: center;
  }
  .service__badge { display: block; margin: 0 auto; }
  .service__name { margin-top: 16px; font-weight: 600; font-size: 17px; }
  .service__phone {
    margin-top: 9px; font-size: 13px;
    display: flex; justify-content: center; align-items: center; gap: 8px;
  }
  .url-pill {
    position: absolute; left: 225px; width: 273px; height: 30px;
    border-radius: 8px; background: var(--pill); color: var(--ink);
    font-size: 15px; text-align: center; line-height: 30px;
  }
  .insert--services .url-pill { top: 470px; }
  .insert--home .url-pill { top: 475px; }
</style>
</head>
<body>

<section class="insert insert--services">
  <div class="insert__photo" role="img" aria-label="Blurred evening street with umbrella and warm bokeh lights"></div>
  <div class="brand">PLUME</div>
  <h1 class="headline">PICK AND DELIVERY SERVICES IN YOUR NEIGHBORHOOD</h1>

  <div class="service" style="left:41px">
    <svg class="service__badge" width="128" height="128" viewBox="0 0 128 128">
      <circle cx="64" cy="64" r="61" fill="rgba(255,255,255,.08)" stroke="#fff" stroke-width="4"/>
      <path d="M64 36c0-6 8-6 8-1 0 4-8 5-8 10 L34 62 H94 L64 45" fill="none" stroke="#fff" stroke-width="3" stroke-linejoin="round"/>
      <rect x="44" y="62" width="40" height="38" fill="#fff"/>
    </svg>
    <div class="service__name">LAUNDRY PICKUP</div>
    <div class="service__phone">
      <svg width="14" height="14" viewBox="0 0 14 14"><circle cx="7" cy="7" r="6" fill="none" stroke="#fff" stroke-width="1.2"/><path d="M4.6 4.2l1.2-.3.7 1.6-.8.6c.4.9 1 1.5 1.9 1.9l.6-.8 1.6.7-.3 1.2c-2.7 0-4.9-2.2-4.9-4.9z" fill="#fff"/></svg>
      +9714-382-7160
    </div>
  </div>

  <div class="service" style="left:252px">
    <svg class="service__badge" width="128" height="128" viewBox="0 0 128 128">
      <circle cx="64" cy="64" r="61" fill="rgba(255,255,255,.08)" stroke="#fff" stroke-width="4"/>
      <path d="M48 58 L60 38 M80 58 L68 38" stroke="#fff" stroke-width="4" stroke-linecap="round"/>
      <path d="M34 58 H94 L88 86 H40 Z" fill="none" stroke="#fff" stroke-width="4" stroke-linejoin="round"/>
      <path d="M50 66v14 M58 66v14 M66 66v14 M74 66v14 M82 66v14" stroke="#fff" stroke-width="4" stroke-linecap="round"/>
    </svg>
    <div class="service__name">GROCERIES DELIVERY</div>
    <div class="service__phone">
      <svg width="14" height="14" viewBox="0 0 14 14"><circle cx="7" cy="7" r="6" fill="none" stroke="#fff" stroke-width="1.2"/><path d="M4.6 4.2l1.2-.3.7 1.6-.8.6c.4.9 1 1.5 1.9 1.9l.6-.8 1.6.7-.3 1.2c-2.7 0-4.9-2.2-4.9-4.9z" fill="#fff"/></svg>
      +9714-382-7160
    </div>
  </div>

  <div class="service" style="left:465px">
    <svg class="service__badge" width="128" height="128" viewBox="0 0 128 128">
      <circle cx="64" cy="64" r="61" fill="rgba(255,255,255,.08)" stroke="#fff" stroke-width="4"/>
      <circle cx="64" cy="41" r="4" fill="#fff"/>
      <path d="M32 76 A32 32 0 0 1 96 76 Z" fill="#fff"/>
      <rect x="26" y="80" width="76" height="5" fill="#fff"/>
    </svg>
    <div class="service__name">RESTAURANTS DELIVERY</div>
    <div class="service__phone">
      <svg width="14" height="14" viewBox="0 0 14 14"><circle cx="7" cy="7" r="6" fill="none" stroke="#fff" stroke-width="1.2"/><path d="M4.6 4.2l1.2-.3.7 1.6-.8.6c.4.9 1 1.5 1.9 1.9l.6-.8 1.6.7-.3 1.2c-2.7 0-4.9-2.2-4.9-4.9z" fill="#fff"/></svg>
      +9714-382-7160
    </div>
  </div>

  <div class="url-pill">www.plumeresidence.com</div>
</section>

<section class="insert insert--home">
  <div class="insert__photo" role="img" aria-label="Lit candles with spa stones and flowers on a wooden table"></div>
  <div class="brand">PLUME</div>
  <h2 class="headline">FEEL AT HOME</h2>
  <p class="lede">Dim the lights, light up a candle, play nice music, have a relaxing stay.</p>
  <div class="url-pill">www.plumeresidence.com</div>
</section>

</body>
</html>
```